Verdanix Medical Business Card

Create a high class Business card for Medical Aesthetics and Wellness Practice called Verdanix Medical Aesthetics and Wellness as per the logo attached.
Addresss is: 418 Harlan Brook Road Suite 312 Melville, New York 11093
Phone (555)204-7391 IG @verdanix_medical
Verdanixmedical.example

I need 5 different name configurations
1) Dr. Theo Valcourt
Aesthetics and Wellness Specialist
Medical Director

2) Rosalind Pettinger, NP
Clinical Nurse Manager

3) Marla Vostrik, RN
Aesthetic Nurse Specialist

4) Petra Halvesen, RN

5) Dana Kowbeck, L.E.
Senior Licensed Esthetician

Target Market(s)

22-55 Females

Industry/Entity Type

Medical Spa and Wellness

Contact Information for Business Card

Logo, address, phone, web, instagram, providers name

Requirements
Must have
• Attractive classy modern look

```html
<!DOCTYPE html>
<html lang="en">
<head>
<meta charset="utf-8">
<title>Verdanix Medical Business Card</title>
<link href="https://fonts.googleapis.com/css2?family=Cinzel:wght@400&family=Cormorant+Garamond:wght@400&family=Source+Serif+4:wght@400;500&display=swap" rel="stylesheet">
<style>
  :root {
    --page: #e6e6e4;
    --card-dark: #201e1c;
    --card-band: #1a1816;
    --card-light: #f7f7f6;
    --gold: #b48a5e;
    --gold-soft: #c29a6c;
    --ink: #1e1e1e;
    --ink-soft: #4a4a4a;
    --rule: #8a8a8a;
  }
  * { margin: 0; padding: 0; box-sizing: border-box; }
  html, body { width: 1200px; height: 1200px; overflow: hidden; }
  body { background: var(--page); position: relative; }

  .card { position: absolute; }

  /* Front */
  .card-front {
    left: 154px; top: 58px; width: 914px; height: 524px;
    background: var(--card-dark);
  }
  .side-band { position: absolute; top: 0; height: 100%; background: var(--card-band); }
  .side-band.left { left: 0; width: 194px; }
  .side-band.right { left: 726px; width: 188px; }
  .gold-rule { position: absolute; top: 0; width: 2px; height: 100%; background: var(--gold); opacity: .85; }
  .gold-rule.left { left: 218px; }
  .gold-rule.right { left: 700px; }

  .ornament { position: absolute; background: var(--gold); opacity: .55; border-radius: 40px; }
  .card-front .ornament.top { left: 360px; top: 96px; width: 196px; height: 52px; }
  .card-front .ornament.bottom { left: 360px; top: 378px; width: 196px; height: 52px; }

  .wordmark {
    position: absolute; left: 0; width: 100%; top: 178px;
    text-align: center;
    font-family: "Cormorant Garamond", serif; font-weight: 400;
    font-size: 66px; letter-spacing: 5px; color: var(--gold);
    line-height: 1;
  }
  .tagline {
    position: absolute; left: 0; width: 100%; top: 278px;
    text-align: center;
    font-family: "Cinzel", serif; font-size: 19px; letter-spacing: 1px;
    color: var(--gold-soft);
  }
  .locale {
    position: absolute; left: 0; width: 100%; top: 314px;
    text-align: center;
    font-family: "Cinzel", serif; font-size: 13px; letter-spacing: 7px;
    color: var(--gold-soft);
  }

  /* Back */
  .card-back {
    left: 172px; top: 620px; width: 884px; height: 506px;
    background: var(--card-light);
    font-family: "Source Serif 4", serif;
  }
  .provider { position: absolute; left: 120px; width: 340px; top: 170px; text-align: center; }
  .provider-name { font-size: 30px; font-weight: 500; color: var(--ink); line-height: 1.1; }
  .provider-role { margin-top: 12px; font-size: 14.5px; color: var(--ink-soft); line-height: 1.45; letter-spacing: .3px; }
  .card-back .ornament { left: 170px; top: 270px; width: 224px; height: 62px; opacity: .6; }

  .divider { position: absolute; left: 466px; top: 158px; width: 1.5px; height: 194px; background: var(--rule); }

  .contact-list { position: absolute; left: 478px; top: 160px; list-style: none; }
  .contact-item { display: flex; align-items: flex-start; color: var(--ink-soft); font-size: 17.5px; letter-spacing: .6px; line-height: 1.2; margin-bottom: 13px; }
  .contact-item.address { margin-top: 8px; line-height: 1.65; }
  .contact-icon { width: 20px; height: 20px; flex: none; margin-right: 10px; margin-top: 1px; }
  .address .contact-icon { margin-top: 5px; }
</style>
</head>
<body>

<section class="card card-front" aria-label="Card front">
  <div class="side-band left" role="img" aria-label="Dark decorative pattern band"></div>
  <div class="side-band right" role="img" aria-label="Dark decorative pattern band"></div>
  <div class="gold-rule left"></div>
  <div class="gold-rule right"></div>
  <div class="ornament top" role="img" aria-label="Gold flourish ornament"></div>
  <h1 class="wordmark">verdanix</h1>
  <p class="tagline">MEDICAL AESTHETICS AND WELLNESS</p>
  <p class="locale">NEW YORK</p>
  <div class="ornament bottom" role="img" aria-label="Gold flourish ornament"></div>
</section>

<section class="card card-back" aria-label="Card back">
  <div class="provider">
    <h2 class="provider-name">Dr. Theo Valcourt</h2>
    <p class="provider-role">Aesthetics and Wellness Specialist<br>Medical Director</p>
  </div>
  <div class="ornament" role="img" aria-label="Gold flourish ornament"></div>

  <div class="divider"></div>

  <ul class="contact-list">
    <li class="contact-item">
      <svg class="contact-icon" viewBox="0 0 20 20" aria-hidden="true">
        <rect width="20" height="20" rx="2" fill="#b48a5e"/>
        <path d="M6 4.5c.6-.4 1.3-.2 1.6.4l.9 1.7c.3.5.1 1.1-.3 1.4l-.7.5c.6 1.5 1.6 2.6 3 3.3l.5-.7c.3-.4.9-.6 1.4-.3l1.7.9c.6.3.8 1 .4 1.6l-.6.9c-.5.6-1.3.9-2.1.6C8.5 13.6 6.2 11.2 5 8c-.3-.8 0-1.7.6-2.1z" fill="#f7f7f6"/>
      </svg>
      <span>(555)204-7391</span>
    </li>
    <li class="contact-item">
      <svg class="contact-icon" viewBox="0 0 20 20" aria-hidden="true">
        <rect width="20" height="20" rx="2" fill="#b48a5e"/>
        <rect x="4" y="6" width="12" height="8.5" fill="none" stroke="#f7f7f6" stroke-width="1.3"/>
        <path d="M4 6l6 5 6-5" fill="none" stroke="#f7f7f6" stroke-width="1.3"/>
      </svg>
      <span>Verdanixmedical.example</span>
    </li>
    <li class="contact-item">
      <svg class="contact-icon" viewBox="0 0 20 20" aria-hidden="true">
        <rect width="20" height="20" rx="2" fill="#b48a5e"/>
      </svg>
      <span>verdanix_medical</span>
    </li>
    <li class="contact-item address">
      <svg class="contact-icon" viewBox="0 0 20 20" aria-hidden="true">
        <rect width="20" height="20" rx="2" fill="#b48a5e"/>
        <path d="M10 3.8a4 4 0 0 1 4 4c0 3-4 7.6-4 7.6S6 10.8 6 7.8a4 4 0 0 1 4-4z" fill="#f7f7f6"/>
        <circle cx="10" cy="7.8" r="1.5" fill="#b48a5e"/>
      </svg>
      <span>418 Harlan Brook Road<br>Suite 312 Melville<br>New York 11093</span>
    </li>
  </ul>
</section>

</body>
</html>
```